Flyer-Design Immobilienmaklerin Tippgeber Provision
Vielen Dank für das ausgezeichnete Flyer-Design! Selma ist eine sehr freundliche und kompetente Web-Designerin. Die Zusammenarbeit war sehr angenehm! Ich kann Sie wärmstes empfehlen und werde bei Bedarf definitiv wieder auf sie zukommen!
Zielgruppe
www.belvoro-immobilien.de (noch nicht ganz fertig)
Hallo, wir sind Immobilienmaklerinnen die noch nicht ganz so lange dabei sind und noch etwas Unterstützung im Bereich Marketing benötigen. Aus diesem Grund möchten wir einen hochwertigen Flyer designen lassen, welches zu uns widerspiegelt und gleichzeitig unsere Zielgruppe (Immobilienbesitzer) anspricht.
Wir sind offen für alle Vorschläge.
Vielen Dank & LG
Marle
BELVORO Immobilien
Aufgabenstellung
- Format: Flyer DIN lang: 105 x 210 mm (QUER)
- Farben: siehe Webseite www.belvoro-immobilien.de
- Das Design sollte professionell, modern und ansprechend sein, nicht zu viel schnick schnack
- QR Code von der Webseite integrieren
- Wir benötigen eine änderbare Datei um ggf. Texte oder Bilder anzupassen im Nachhinein
- Bildmaterial beigefügt, weitere Bilder von Häusern etc. bitte selbst recherchieren
TEXTE:
Tippgeber Provision
UNSER DANKESCHÖN AN SIE
Sie kennen jemanden, der seine Immobilie verkaufen oder vermieten möchte?
Dann geben Sie uns diesen Tipp weiter und erhalten dafür 10% Tippgeber Provision aus unserer verdienten Brutto-Provision.
Der Ablauf ist wie folgt:
1. Tipp & Kontakt
Sie erfahren von einem geplanten Immobilien-Verkauf (z.B. in Ihrer Nachbarschaft oder bei Freunden) und stellen uns den Kontakt zu den Eigentümern her
2. Vertrag
Wir schließen mit dem Immobilien-Eigentümer einen Maklervertrag
3. Erfolgreiche Vermittlung
Die Immobilie wird von uns erfolgreich vermittelt
4. Tippgeber-Provision
Sobald wir für die erfolgreiche Vermittlung unser Honorar erhalten haben, reichen wir Ihnen Ihre Tippgeber Provision in Höhe von 10% weiter
(in klein)
Voraussetzungen:
Die Immobilie ist uns bisher unbekannt
Die Immobilie wurde noch nicht öffentlich zum Verkauf ausgeschrieben (z.B. in Zeitungen, Internetportale, durch Verkaufsschilder etc.)
Die Immobilie befindet sich im Großraum Hannover
Ihre Immobilienexpertinnen,
Berit Olsenka & Marlene Voskowitz
info@belvoro-immobilien.de
www.belvoro-immobilien.de
INFOS ZUM UNTERNEHMEN:
Über uns
Wir sind ein junges dynamisches Gespann, welches voll und ganz auf die Wünsche und Bedürfnisse unserer Kunden eingeht. Gemeinsam mit Ihnen holen wir das Bestmögliche aus Ihrer Immobilie raus. Wir arbeiten stets wertorientiert und kultur..

```html
<!DOCTYPE html>
<html lang="de">
<head>
<meta charset="utf-8">
<title>BELVORO Immobilien – Tippgeber Provision Flyer</title>
<link href="https://fonts.googleapis.com/css2?family=Marcellus&family=Montserrat:wght@300;400;500;600;700&display=swap" rel="stylesheet">
<style>
:root{
  --copper:#cf906c;
  --copper-dark:#b97a57;
  --ink:#5a5a5a;
  --ink-dark:#3b3b3b;
  --band:#2a2626;
  --label:#555556;
  --paper:#ffffff;
  --stage:#e7e7e7;
  --serif:'Marcellus', 'Times New Roman', serif;
  --sans:'Montserrat', Arial, sans-serif;
}
*{margin:0;padding:0;box-sizing:border-box}
html,body{width:720px;height:1200px;overflow:hidden;background:var(--stage)}
h1,h2,h3{font-weight:400}
.flyer{position:absolute;left:20px;width:680px;height:340px;background:var(--paper);overflow:hidden;box-shadow:0 4px 14px rgba(0,0,0,.18);font-family:var(--sans);color:var(--ink)}
.flyer--front{top:190px}
.flyer--back{top:640px}
.abs{position:absolute}
.shape{position:absolute;left:0;top:0}

/* front */
.headline{left:24px;top:8px;font-family:var(--serif);font-weight:400;color:var(--ink);font-size:41px;line-height:35px;letter-spacing:.5px}
.headline .sub{font-family:var(--sans);font-weight:300;color:var(--copper);font-size:25px;letter-spacing:2.4px;border-bottom:1px solid var(--copper);padding-bottom:1px;margin-left:6px;position:relative;top:-3px}
.question{left:23px;top:92px;width:408px;height:18px;border-radius:6px;background:var(--copper);color:#fff;font-weight:600;font-size:10px;line-height:18px;text-align:center;white-space:nowrap}
.intro{left:23px;top:123px;width:400px;font-size:6.6px;line-height:10px}
.intro b{font-weight:700}
.steps{left:22px;top:153px;width:370px}
.step{position:absolute;left:0;width:370px}
.step .icon{position:absolute;left:2px;top:0;width:22px;height:22px}
.step h3{position:absolute;left:37px;top:0;font-family:var(--serif);font-weight:400;color:var(--copper);font-size:11px;letter-spacing:.3px;white-space:nowrap}
.step p{position:absolute;left:37px;top:13px;width:330px;font-size:6.4px;line-height:10px}
.connector{position:absolute;left:13px;width:0;border-left:1px dotted var(--ink)}
.terms{left:22px;top:301px;width:340px;font-size:4.3px;line-height:5.6px}
.contact{left:22px;top:324px;color:#fff;font-size:7px;font-weight:500;display:flex;gap:10px;align-items:center}
.contact span{display:flex;align-items:center;gap:3px}
.photo{background:linear-gradient(100deg,#e6ddd3 0%,#cdb9a5 35%,#8f735e 60%,#6b5647 100%)}
.brand{color:#fff;font-family:var(--serif);text-align:center;white-space:nowrap}
.brand .name{font-size:26px;line-height:28px;letter-spacing:.5px}
.brand .kind{font-size:7.5px;letter-spacing:5px;line-height:12px;padding-left:5px}
.role{left:497px;top:281px;width:183px;height:17px;background:var(--label);color:#fff;font-size:10px;font-weight:500;line-height:17px;padding-left:8px;white-space:nowrap}
.names{left:464px;top:303px;width:193px;height:19px;border-radius:5px;background:var(--copper);color:#fff;font-size:10px;font-weight:500;line-height:19px;text-align:center;white-space:nowrap}

/* back */
.section-title{position:absolute;left:22px;font-family:var(--serif);font-weight:400;font-size:10.5px;color:var(--ink);width:420px;border-bottom:1px solid var(--copper);padding-bottom:4px}
.body{position:absolute;left:22px;width:420px;font-size:6.1px;line-height:10.3px}
.cta{right:12px;top:66px;color:#fff;font-family:var(--serif);font-size:9px;line-height:13.5px;text-align:right}
.mail{left:522px;top:116px;width:158px;height:18px;background:var(--label);color:#fff;font-size:8.5px;font-weight:500;line-height:18px;padding-left:7px;white-space:nowrap}
.brand--back{left:446px;top:70px;width:124px;color:var(--ink-dark)}
.brand--back .name{font-size:23px;line-height:25px}
.brand--back .kind{font-size:7px;letter-spacing:4.4px}
.services{left:0;top:319px;width:680px;height:21px;background:var(--band);color:#fff;font-size:5.9px;font-weight:500;line-height:21px;padding-left:22px;white-space:nowrap}
</style>
</head>
<body>

<section class="flyer flyer--front" aria-label="Vorderseite">
  <svg class="shape" width="680" height="340" viewBox="0 0 680 340">
    <polygon points="546,0 680,0 680,340 342,340" fill="var(--copper)"/>
    <polygon points="0,317 356,317 342,340 0,340" fill="var(--band)"/>
  </svg>

  <div class="abs photo" role="img" aria-label="Porträtfoto der zwei Immobilienexpertinnen vor kupferfarbenem Hintergrund" style="left:372px;top:112px;width:300px;height:228px;clip-path:polygon(18% 0,100% 0,100% 100%,0 100%,5% 40%)"></div>

  <div class="abs brand" style="left:540px;top:62px;width:130px">
    <div class="name">BELVORO</div>
    <div class="kind">IMMOBILIEN</div>
  </div>

  <h1 class="abs headline">UNSER DANKESCHÖN<br>AN SIE!<span class="sub">Tippgeber Provision</span></h1>

  <div class="abs question">Sie kennen jemanden, der seine Immobilie verkaufen oder vermieten möchte?</div>

  <p class="abs intro">Dann geben Sie uns diesen Tipp weiter und erhalten dafür 10% Tippgeber Provision aus unserer verdienten Brutto-Provision. <b>So funktioniert es:</b></p>

  <div class="abs steps">
    <div class="connector" style="top:25px;height:16px"></div>
    <div class="connector" style="top:66px;height:11px"></div>
    <div class="connector" style="top:101px;height:10px"></div>

    <div class="step" style="top:0">
      <svg class="icon" viewBox="0 0 22 22"><ellipse cx="9" cy="8" rx="8" ry="6.5" fill="var(--copper)"/><path d="M4 13 L3 17 L8 14Z" fill="var(--copper)"/><ellipse cx="15" cy="13" rx="6" ry="5" fill="var(--copper-dark)"/><path d="M18 17 L20 20 L15 18Z" fill="var(--copper-dark)"/></svg>
      <h3>TIPP UND KONTAKT</h3>
      <p>Sie erfahren von einem geplanten Immobilien-Verkauf (z.B. in Ihrer Nachbarschaft oder bei Freunden) und stellen uns den Kontakt zu den Eigentümern her</p>
    </div>
    <div class="step" style="top:44px">
      <svg class="icon" viewBox="0 0 22 22"><rect x="4" y="3" width="14" height="18" rx="1.5" fill="var(--copper)"/><rect x="8" y="1" width="6" height="4" rx="1" fill="var(--copper-dark)"/><g stroke="#fff" stroke-width="1.2"><line x1="7" y1="9" x2="15" y2="9"/><line x1="7" y1="12.5" x2="15" y2="12.5"/><line x1="7" y1="16" x2="15" y2="16"/></g></svg>
      <h3>VERTRAG</h3>
      <p>Wir schließen mit dem Immobilien-Eigentümer einen Maklervertrag</p>
    </div>
    <div class="step" style="top:80px">
      <svg class="icon" viewBox="0 0 22 22"><path d="M1 8 L6 5 L11 9 L16 5 L21 8 L17 14 L12 18 L6 14Z" fill="var(--copper)"/><path d="M7 10 L11 13 L15 10" stroke="#fff" stroke-width="1.2" fill="none"/></svg>
      <h3>ERFOLGREICHE VERMITTLUNG</h3>
      <p>Die Immobilie wird von uns erfolgreich vermittelt</p>
    </div>
    <div class="step" style="top:110px">
      <svg class="icon" viewBox="0 0 22 22"><rect x="3" y="8" width="16" height="4" fill="var(--copper)"/><rect x="4" y="13" width="14" height="8" fill="var(--copper)"/><rect x="10" y="8" width="2" height="13" fill="#fff"/><path d="M11 8 C7 2 4 5 8 8 M11 8 C15 2 18 5 14 8" stroke="var(--copper)" stroke-width="1.5" fill="none"/></svg>
      <h3>TIPPGEBER-PROVISION</h3>
      <p>Sobald wir für die erfolgreiche Vermittlung unser Honorar erhalten haben, reichen wir Ihnen Ihre Tippgeber Provision in Höhe von 10% weiter</p>
    </div>
  </div>

  <p class="abs terms">Voraussetzungen: Die Immobilie ist uns bisher unbekannt. Die Immobilie wurde noch nicht öffentlich zum Verkauf ausgeschrieben (z.B. in Zeitungen, Internetportale, durch Verkaufsschilder etc.). Die Immobilie befindet sich im Großraum Hannover</p>

  <div class="abs contact">
    <span><svg width="7" height="5" viewBox="0 0 7 5"><rect width="7" height="5" fill="#fff"/><path d="M0 0 L3.5 3 L7 0" stroke="var(--band)" stroke-width=".7" fill="none"/></svg>info@belvoro-immobilien.de</span>
    <span><svg width="6" height="6" viewBox="0 0 6 6"><path d="M1 0 L2.3 0 L2.8 1.6 L2 2.3 Q2.8 3.6 3.7 4 L4.4 3.2 L6 3.7 L6 5 Q5.5 6 4.4 6 Q0 4.5 0 1.3 Q0 0 1 0Z" fill="#fff"/></svg>0511 48203917</span>
    <span><svg width="7" height="7" viewBox="0 0 7 7"><circle cx="3.5" cy="3.5" r="3" stroke="#fff" stroke-width=".7" fill="none"/><ellipse cx="3.5" cy="3.5" rx="1.3" ry="3" stroke="#fff" stroke-width=".6" fill="none"/><line x1=".5" y1="3.5" x2="6.5" y2="3.5" stroke="#fff" stroke-width=".6"/></svg>www.belvoro-immobilien.de</span>
  </div>

  <div class="abs role">Ihre Immobilienexpertinnen</div>
  <div class="abs names">Berit Olsenka &amp; Marlene Voskowitz</div>
</section>

<section class="flyer flyer--back" aria-label="Rückseite">
  <svg class="shape" width="680" height="340" viewBox="0 0 680 340">
    <polygon points="640,0 680,0 680,319 445,319 445,200 560,130" fill="var(--copper)"/>
  </svg>

  <h2 class="section-title" style="top:13px">ÜBER UNS</h2>
  <p class="body" style="top:38px">Wir sind ein junges dynamisches Gespann, welches voll und ganz auf die Wünsche und Bedürfnisse unserer Kunden eingeht. Gemeinsam mit Ihnen holen wir das Bestmögliche aus Ihrer Immobilie raus. Wir arbeiten stets wertorientiert und kulturoffen und freuen uns auf jede neue Herausforderung. Das eigene Zuhause soll für unsere Kunden der Rückzugsort und die Wohlfühloase werden. Ob mieten oder kaufen, wir suchen Ihnen diesen speziellen Ort.</p>

  <h2 class="section-title" style="top:91px">UNSER SERVICE</h2>
  <p class="body" style="top:116px">Immobilien sind viel mehr als nur Bauwerke aus Stein und Mörtel. Die Immobilien Güter sind eng mit Erinnerungen, Träumen und Gefühlen verbunden. Ihre Bewohner füllen sie mit Leben und geben ihnen Mehrwert. Ihre Makler von BELVORO Immobilien wissen das. Für uns geht es nicht nur um Immobilien, sondern auch um die Menschen dahinter. Deswegen widmen wir uns Immobiliengeschäften ganzheitlich und mit Weitsicht.</p>
  <p class="body" style="top:163px">Ob Immobilienkauf, Immobilienvermietung oder Immobilienverkauf: Sie als Kunde stehen für uns im Fokus. Ehrlich, seriös und allumfassend beraten wir Sie. Dabei agieren Ihre Anforderungen als Kompass für unser transparentes Handeln. Lernen Sie uns kennen!</p>

  <h2 class="section-title" style="top:205px">FACHWISSEN TRIFFT AUF ERFAHRUNG UND ENGAGEMENT</h2>
  <p class="body" style="top:231px">Erfolg in Immobiliengeschäften ist kein Zufall. Fachwissen fusioniert mit Erfahrung und Engagement, um die besten Ergebnisse zu erzielen.</p>
  <p class="body" style="top:257px">Ihre Makler von BELVORO Immobilien setzen sich für Sie und Ihre Belange ein. Bei uns profitieren Sie von einem professionellen Vorgehen und einer aufrichtigen Leidenschaft für den Job. Unsere Beratung ist bedarfs- und zielorientiert. An einer großen Portion an Feingefühl und Empathie mangelt es nicht. Kontaktieren Sie uns für einen zuverlässigen Immobilienservice in Isernhagen!</p>

  <div class="abs brand brand--back">
    <div class="name">BELVORO</div>
    <div class="kind">IMMOBILIEN</div>
  </div>

  <p class="abs cta">SCHREIBEN<br>SIE UNS BEI<br>INTERESSE AN</p>
  <div class="abs mail">info@belvoro-immobilien.de</div>

  <div class="abs photo" role="img" aria-label="Foto der dunkelhaarigen Maklerin mit verschränkten Armen" style="left:460px;top:142px;width:102px;height:167px;background:linear-gradient(160deg,#9a9a93 0%,#7a6a55 45%,#5a4a38 100%)"></div>
  <div class="abs photo" role="img" aria-label="Foto der blonden Maklerin mit verschränkten Armen" style="left:567px;top:142px;width:101px;height:167px;background:linear-gradient(160deg,#a9a7a2 0%,#c7a38a 50%,#b07b58 100%)"></div>

  <div class="abs services">Verkauf und Vermietung · Kostenlose Wertermittlung · Erstellung eines Exposés · Erstellung des Energieausweises · Home Staging · Open-House-Besichtigungen · Sanierung von Wohnräumen</div>
</section>

</body>
</html>
```